GHollis Busisness Card

I am an aerospace consultant and at this time only need business cards.

Industry/Entity Type

Business

Contact Information for Business Card

Hollis Partners,LLC
Gerald T. Hollis

348 Birch Hollow Road
Madison AL 35762

256-555-0148 (cell)
256-555-0173 (fax)

geraldhollis@mailbrook.net

```html
<!DOCTYPE html>
<html lang="en">
<head>
<meta charset="UTF-8">
<title>Hollis Partners LLC – Business Card</title>
<link rel="stylesheet" href="https://fonts.googleapis.com/css2?family=Montserrat:wght@500;600&display=swap">
<style>
  :root {
    --backdrop: #e6e6e2;
    --card-light: #ffffff;
    --card-shade: #e4e4e4;
    --brand-blue: #2f63b0;
    --ink: #1b1b1b;
  }
  * { margin: 0; padding: 0; box-sizing: border-box; }
  html, body {
    width: 1200px;
    height: 800px;
    overflow: hidden;
    background: var(--backdrop);
    font-family: "Montserrat", sans-serif;
  }
  .canvas {
    position: relative;
    width: 1200px;
    height: 800px;
  }
  .card {
    position: absolute;
    width: 520px;
    height: 297px;
    background: linear-gradient(135deg, var(--card-light) 0%, #f3f3f3 55%, var(--card-shade) 100%);
    box-shadow: 0 6px 18px rgba(0, 0, 0, 0.18);
    overflow: hidden;
  }
  .card--front { left: 60px; top: 70px; }
  .card--back { left: 620px; top: 430px; }

  .stripe {
    position: absolute;
    left: 0;
    right: 0;
    height: 6px;
    background: var(--brand-blue);
  }
  .stripe--top { top: 16px; }
  .stripe--bottom { bottom: 16px; }

  .wordmark { line-height: 1.15; }
  .wordmark__name {
    display: block;
    color: var(--brand-blue);
    font-weight: 600;
  }
  .wordmark__suffix {
    display: block;
    color: var(--ink);
    font-weight: 500;
  }

  .card--front .wordmark {
    position: absolute;
    left: 0;
    right: 0;
    top: 112px;
    text-align: center;
  }
  .card--front .wordmark__name { font-size: 24px; }
  .card--front .wordmark__suffix { font-size: 19px; }

  .card--back .wordmark {
    position: absolute;
    left: 38px;
    top: 150px;
  }
  .card--back .wordmark__name { font-size: 28px; }
  .card--back .wordmark__suffix { font-size: 21px; }

  .contact-list {
    position: absolute;
    left: 268px;
    top: 62px;
    list-style: none;
  }
  .contact-item {
    display: flex;
    align-items: flex-start;
    gap: 10px;
    margin-bottom: 12px;
    font-size: 10.5px;
    font-weight: 500;
    color: var(--ink);
    line-height: 1.3;
  }
  .contact-item__icon {
    flex: none;
    width: 22px;
    height: 22px;
  }
  .contact-item__text { padding-top: 2px; }
</style>
</head>
<body>
<main class="canvas">

  <section class="card card--front" aria-label="Business card front">
    <div class="stripe stripe--top"></div>
    <div class="wordmark">
      <span class="wordmark__name">Hollis</span>
      <span class="wordmark__suffix">Partners LLC</span>
    </div>
    <div class="stripe stripe--bottom"></div>
  </section>

  <section class="card card--back" aria-label="Business card back">
    <div class="stripe stripe--top"></div>

    <div class="wordmark">
      <span class="wordmark__name">Hollis</span>
      <span class="wordmark__suffix">Partners LLC</span>
    </div>

    <ul class="contact-list">
      <li class="contact-item">
        <svg class="contact-item__icon" viewBox="0 0 22 22" aria-hidden="true">
          <rect x="1" y="1" width="20" height="20" fill="none" stroke="#2f63b0" stroke-width="1.5"/>
          <circle cx="11" cy="8.5" r="3" fill="#2f63b0"/>
          <path d="M5.5 17 Q11 10.5 16.5 17 Z" fill="#2f63b0"/>
        </svg>
        <span class="contact-item__text">Gerald T. Hollis</span>
      </li>
      <li class="contact-item">
        <svg class="contact-item__icon" viewBox="0 0 22 22" aria-hidden="true">
          <rect x="1" y="1" width="20" height="20" fill="none" stroke="#2f63b0" stroke-width="1.5"/>
          <path d="M11 17.5 C7.5 13 7 11.5 7 9.5 A4 4 0 0 1 15 9.5 C15 11.5 14.5 13 11 17.5 Z" fill="none" stroke="#2f63b0" stroke-width="1.5"/>
          <circle cx="11" cy="9.5" r="1.4" fill="#2f63b0"/>
        </svg>
        <span class="contact-item__text">348 Birch Hollow Road Madison<br>AL 35762</span>
      </li>
      <li class="contact-item">
        <svg class="contact-item__icon" viewBox="0 0 22 22" aria-hidden="true">
          <rect x="1" y="1" width="20" height="20" fill="none" stroke="#2f63b0" stroke-width="1.5"/>
          <path d="M7 5.5 L9 5.5 L10 8.5 L8.7 9.6 C9.4 11.3 10.7 12.6 12.4 13.3 L13.5 12 L16.5 13 L16.5 15 C16.5 15.8 15.8 16.5 15 16.5 C10 16.2 5.8 12 5.5 7 C5.5 6.2 6.2 5.5 7 5.5 Z" fill="#2f63b0"/>
        </svg>
        <span class="contact-item__text">256-555-0148<br>FAX: 256-555-0173</span>
      </li>
      <li class="contact-item">
        <svg class="contact-item__icon" viewBox="0 0 22 22" aria-hidden="true">
          <rect x="1" y="1" width="20" height="20" fill="none" stroke="#2f63b0" stroke-width="1.5"/>
          <rect x="5" y="7" width="12" height="8.5" fill="#2f63b0"/>
          <path d="M5 7 L11 12 L17 7" fill="none" stroke="#ffffff" stroke-width="1.2"/>
        </svg>
        <span class="contact-item__text">geraldhollis@mailbrook.net</span>
      </li>
    </ul>

    <div class="stripe stripe--bottom"></div>
  </section>

</main>
</body>
</html>
```